Strong, Clean Book Design Needed for "The Lantern Keeper"

I need a strong, clean, masculine cover of a book that focuses on helping men restore honor to what it means to be a good husband. (I also need a back cover and spine done as well). I would like the cover to be either a white, red, or black cover. I have attached 3 books that I would like to use as examples to model after. I also attached a word document to show the potential layouts I would like to see and how that parallel the example covers.

Specs:
- Book is 150 pages long
- Size is 5.25 x 8

Target Market(s)

Christian men who are married or looking to be married.

Font styles to use
Serif
Sans Serif

Colors
ec1f27
f04a50
ffffff
000000
1b1b1b
757575

Requirements
Must have
• - A design that resembles/has a similar feel to one of the three examples that are attached and laid out similarly to one of the 3 designs in the word doc "3 Book Designs"
• - These elements on the front cover: Title: The Lantern Keeper, Subtitle: Restoring the honor of a Christ-centered marriage, Author Name: Dean Halvorsen
• - A strong design that is simple yet creative.
• - Strong masculine font that is bold but not too flashy
• - Red should be included either as the title font color or as the overall cover color.
• - The back of the book should have the attached file "Back of the book" text on the back
Nice to have
• - A color contrast, like a strip of another color (see "example 3" attached file) across the front for the subtitle or the author name.
• - Including the attached sword file as a somewhat transparent image on the cover, but absolutely not necessary.
• - If there is going to be any highlighting of words in the subtitle, they should be the word "honor" and "Christ-centered"
Should not have
• Any religious symbols, such as a cross.

```html
<!DOCTYPE html>
<html lang="en">
<head>
<meta charset="utf-8">
<title>The Lantern Keeper – Book Covers</title>
<link rel="stylesheet" href="https://fonts.googleapis.com/css2?family=Cinzel:wght@400;700&family=Josefin+Sans:wght@700&family=Open+Sans:wght@600;700&display=swap">
<style>
  :root {
    --red: #ec1f27;
    --red-soft: #f04a50;
    --red-deep: #a3121a;
    --red-dark: #7c0c12;
    --white: #ffffff;
    --cream: #f4e9d6;
    --black: #000000;
    --ink: #1b1b1b;
    --grey: #757575;
    --stage: #ececec;
  }
  * { margin: 0; padding: 0; box-sizing: border-box; }
  html, body { width: 1200px; height: 1000px; overflow: hidden; }
  body {
    background: var(--stage);
    position: relative;
    font-family: "Open Sans", Arial, sans-serif;
  }

  .cover {
    position: absolute;
    top: 150px;
    width: 450px;
    height: 700px;
    overflow: hidden;
  }

  /* Back cover */
  .back-cover {
    left: 135px;
    background: radial-gradient(ellipse at 40% 35%, var(--red) 0%, var(--red-deep) 65%, var(--red-dark) 100%);
    color: var(--white);
    padding: 44px 34px 0 38px;
  }
  .back-heading {
    font-family: "Josefin Sans", Arial, sans-serif;
    font-weight: 700;
    color: var(--cream);
    text-transform: uppercase;
    line-height: 1.12;
    letter-spacing: 0.5px;
  }
  .back-heading .line-small { display: block; font-size: 22px; }
  .back-heading .line-large { display: block; font-size: 27px; margin-top: 2px; }
  .back-copy {
    margin-top: 14px;
    font-size: 10.2px;
    font-weight: 600;
    line-height: 1.55;
    text-align: justify;
  }
  .back-copy p + p { margin-top: 12px; }
  .back-copy .closing { font-size: 10.2px; }
  .sword-band {
    display: block;
    margin: 22px 0 0 0;
    width: 360px;
    height: 14px;
    border-radius: 7px;
    background: linear-gradient(90deg, rgba(255,255,255,0.05) 0%, rgba(255,255,255,0.35) 55%, var(--red-dark) 70%, var(--ink) 100%);
  }
  .author-bio {
    margin-top: 38px;
    font-size: 10.6px;
    font-weight: 600;
    line-height: 1.6;
  }
  .author-bio strong { font-weight: 700; }

  /* Front cover */
  .front-cover {
    left: 615px;
    background: var(--white);
    box-shadow: 0 0 0 1px #dcdcdc;
  }
  .sword-visual {
    position: absolute;
    left: 18px;
    top: 0;
    width: 100px;
    height: 700px;
    background: linear-gradient(180deg,
      #ece6d8 0%, #d9d0bd 24%, #a0603a 28%, #6e3a22 33%,
      #3a2a20 38%, #111111 45%, #1b1b1b 75%, #2a1c12 100%);
  }
  .title-block {
    position: absolute;
    right: 26px;
    top: 86px;
    text-align: right;
    font-family: "Josefin Sans", Arial, sans-serif;
    font-weight: 700;
    color: var(--red-deep);
    text-transform: uppercase;
    line-height: 0.95;
  }
  .title-the { display: block; font-size: 150px; letter-spacing: -2px; }
  .title-main { display: block; font-size: 58px; margin-top: 14px; }
  .subtitle {
    position: absolute;
    left: 150px;
    right: 20px;
    top: 492px;
    text-align: center;
    font-family: "Cinzel", Georgia, serif;
    font-size: 15px;
    line-height: 1.35;
    color: var(--ink);
    text-transform: uppercase;
    letter-spacing: 0.5px;
  }
  .subtitle b { font-weight: 700; }
  .author-name {
    position: absolute;
    left: 140px;
    right: 12px;
    top: 584px;
    text-align: center;
    font-family: "Cinzel", Georgia, serif;
    font-weight: 700;
    font-size: 34px;
    color: var(--black);
    text-transform: uppercase;
  }
</style>
</head>
<body>

  <section class="cover back-cover">
    <h2 class="back-heading">
      <span class="line-small">Do you have</span>
      <span class="line-small">what it takes to be</span>
      <span class="line-large">a Lantern Keeper?</span>
    </h2>
    <div class="back-copy">
      <p>The samurai were fearsome Japanese warriors known for their discipline, loyalty, and strict adherence to their code of honor, bushido. Along with their ferocity on the battlefield, they also embodied the heart and sacrifice of “those who serve,” the meaning of the word samurai. The samurai lived, and more importantly, died by the honor that characterized these ideals. The samurai way of life transformed the nation, culture, and moral code of Japan, and continues to do so to this day…</p>
      <p><em>The Lantern Keeper</em> is more than just an interesting read: it is a radically Christ-centered approach to marriage. Dean Halvorsen recaptures what it means to be a man and an effective leader in a marriage by simply, but powerfully, laying out the Biblical qualities found in Ephesians 5 that God calls husbands to embody. With a fresh and unique perspective, Dean parallels how samurai warriors once lived and how godly husbands should live in a way that restores and highlights the honor, sacrifice, and purpose of marriage. This book will undoubtedly shift the way men view and function in their role as a husband and gives them practical nuts and bolts suggestions for day-to-day success as a husband.</p>
      <p>This is a wake-up call to all husbands everywhere: be the man and the husband God has called you to be. Although it is not easy, it is guaranteed to transform your life… and your marriage!</p>
      <p class="closing">Embrace the call of a truly Christ-centered marriage.<br><em>Embrace the way of the Lantern Keeper.</em></p>
    </div>
    <div class="sword-band" role="img" aria-label="Illustration of a sheathed sword lying horizontally"></div>
    <p class="author-bio"><strong>DEAN HALVORSEN</strong> is the Microchurch Pastor at the Harborlight Church in Marlow, Oregon where he has a heart for marriage as well as multiplying disciples and churches. He has a fierce love for all people and has been married to his wife, Ellen, for over a decade. They have two beautiful daughters, Maren and Liesel.</p>
  </section>

  <section class="cover front-cover">
    <div class="sword-visual" role="img" aria-label="Photograph of an upright sword with an ivory carved handle, bronze guard and black scabbard"></div>
    <h1 class="title-block">
      <span class="title-the">The</span>
      <span class="title-main">Lantern</span>
      <span class="title-main">Keeper</span>
    </h1>
    <p class="subtitle">Restoring the <b>honor</b> of a<br><b>Christ-centered</b> marriage</p>
    <p class="author-name">Dean Halvorsen</p>
  </section>

</body>
</html>
```